<作成物>
■リッチメッセージ
リッチメニュー
合計2枚

【デザインの詳細】
デザインの詳細イメージをファイルに入れております。
また、別の業種の方ですが、サンプルデザインをファイルのリンク先に付けておりますのでご確認ください。
上下で一体感があるものを希望します。

〈リッチメニューの表示項目〉
左上から① ホームページ・SNS・自己紹介 ②サービス紹介 ③動画で体験
左下から④オンラインショップ ⑤お客様の声 ⑥お問い合わせ

デザイン重視でここの表示名はデザイン的に英語の方がよければ
英語でも大丈夫です。意味がわかって
ニュアンスがあっていれば文字を短くするのも
お任せします。あくまでデザイン重視です。
〈画像はこちらから〉
素材画像
https://7.kumobako.example/3081-a4f2c9e7b1d05e6f38c2a9d4e7b61f05

※こちらの作成以外に勝手に使用された場合は
著作権侵害で法的手段をとらせていただきます。
作成事例にもしようしないでください。

<サイズ>
・リッチメッセージ(1040×1040ピクセル)
・リッチメニュー(1200×810ピクセル)

<納品形式>
・ai形式(イラストレーターデータ)
・psd形式(フォトショップデータ)
・JPG
<詳細>
※添付ファイルをご確認ください。

<備考>
ブランディング効果を期待しています。
どんどん何個でも応募ください。

```html
<!DOCTYPE html>
<html lang="ja">
<head>
<meta charset="utf-8">
<title>Serenova リッチメッセージ・リッチメニュー</title>
<link rel="stylesheet" href="https://fonts.googleapis.com/css2?family=M+PLUS+Rounded+1c:wght@500;700&family=Noto+Sans+JP:wght@400;500&family=Comfortaa:wght@500&display=swap">
<style>
  :root {
    --ink: #3a3a3a;
    --white: #ffffff;
    --pink: #ee7da3;
    --tile-red: rgba(232, 96, 112, 0.78);
    --tile-teal: rgba(64, 196, 178, 0.78);
    --tile-pink: rgba(226, 96, 150, 0.72);
    --tile-border: rgba(255, 255, 255, 0.85);
  }
  * { margin: 0; padding: 0; box-sizing: border-box; }
  html, body { width: 803px; height: 1200px; overflow: hidden; background: #fff; }
  .canvas { position: relative; width: 803px; height: 1200px; overflow: hidden; font-family: "Noto Sans JP", sans-serif; }

  .message { position: absolute; left: 0; top: 0; width: 803px; height: 690px; }
  .message__art {
    position: absolute; inset: 0;
    background:
      radial-gradient(ellipse 420px 300px at 80% 12%, rgba(246, 150, 170, 0.75), transparent 70%),
      radial-gradient(ellipse 380px 260px at 18% 20%, rgba(250, 215, 130, 0.7), transparent 70%),
      radial-gradient(ellipse 300px 240px at 60% 30%, rgba(190, 170, 230, 0.55), transparent 70%),
      radial-gradient(ellipse 360px 200px at 10% 85%, rgba(170, 220, 235, 0.6), transparent 70%),
      radial-gradient(ellipse 300px 220px at 95% 80%, rgba(252, 205, 120, 0.55), transparent 70%),
      #fdf7f6;
  }
  .message__fade {
    position: absolute; left: 0; top: 340px; width: 803px; height: 290px;
    background: rgba(255, 255, 255, 0.82);
  }
  .tagline {
    position: absolute; left: 0; top: 392px; width: 803px; text-align: center;
    font-family: "M PLUS Rounded 1c", sans-serif; font-weight: 500;
    font-size: 36px; color: var(--ink); letter-spacing: 1px;
  }
  .brand {
    position: absolute; left: 80px; top: 476px; width: 470px; text-align: center;
    font-family: "Comfortaa", sans-serif; font-weight: 500; font-size: 58px; color: var(--ink);
  }
  .brand__kana {
    position: absolute; left: 80px; top: 552px; width: 470px; text-align: center;
    font-family: "Noto Sans JP", sans-serif; font-size: 26px; color: var(--ink); letter-spacing: 3px;
  }
  .badge {
    position: absolute; left: 606px; top: 448px; width: 156px; height: 156px; border-radius: 50%;
    background: var(--pink); color: var(--white); display: flex; flex-direction: column;
    align-items: center; justify-content: center; text-align: center;
    font-size: 21px; line-height: 1.25;
  }

  .menu { position: absolute; left: 0; top: 690px; width: 803px; height: 510px; }
  .menu__art {
    position: absolute; inset: 0;
    background:
      radial-gradient(ellipse 300px 120px at 50% 85%, rgba(120, 170, 220, 0.8), transparent 70%),
      radial-gradient(ellipse 340px 200px at 15% 40%, rgba(255, 210, 60, 0.85), transparent 70%),
      radial-gradient(ellipse 300px 220px at 85% 30%, rgba(120, 210, 235, 0.8), transparent 70%),
      radial-gradient(ellipse 260px 200px at 50% 20%, rgba(250, 140, 170, 0.7), transparent 70%),
      linear-gradient(180deg, #f8c0d0 0%, #b8d8ea 60%, #7fa8d8 100%);
  }
  .tiles {
    position: absolute; left: 22px; top: 16px; width: 760px;
    display: grid; grid-template-columns: repeat(3, 240px); grid-template-rows: repeat(2, 208px);
    gap: 14px 20px;
  }
  .tile {
    border: 3px solid var(--tile-border); border-radius: 8px; color: var(--white);
    display: flex; flex-direction: column; align-items: center; justify-content: flex-start;
    padding-top: 24px; text-align: center;
  }
  .tile--red { background: var(--tile-red); }
  .tile--teal { background: var(--tile-teal); }
  .tile--pink { background: var(--tile-pink); }
  .tile__icon { width: 74px; height: 74px; margin-bottom: 10px; }
  .tile__label { font-family: "M PLUS Rounded 1c", sans-serif; font-weight: 700; font-size: 24px; line-height: 1.2; }
  .tile__en { font-size: 13px; margin-top: 6px; letter-spacing: 0.5px; }
</style>
</head>
<body>
<div class="canvas">
  <section class="message">
    <div class="message__art" role="img" aria-label="パステルカラーの水彩風背景"></div>
    <div class="message__fade"></div>
    <p class="tagline">“癒しの音”と“エステ”の融合</p>
    <p class="brand">Serenova</p>
    <p class="brand__kana">-セレノヴァ-</p>
    <div class="badge"><span>Crystal bowl</span><span>×</span><span>Himalayan</span><span>therapy</span></div>
  </section>

  <nav class="menu">
    <div class="menu__art" role="img" aria-label="水彩の色彩と水面の波紋の背景"></div>
    <div class="tiles">
      <a class="tile tile--red">
        <svg class="tile__icon" viewBox="0 0 74 74" fill="none" stroke="#fff" stroke-width="5"><rect x="8" y="10" width="58" height="48" rx="3"/><line x1="8" y1="22" x2="66" y2="22"/><rect x="16" y="30" width="18" height="20" fill="#fff" stroke="none"/><line x1="40" y1="33" x2="58" y2="33"/><line x1="40" y1="45" x2="58" y2="45"/></svg>
        <span class="tile__label">ホームページ<br>SNS・自己紹介</span>
        <span class="tile__en">Website / SNS</span>
      </a>
      <a class="tile tile--teal">
        <svg class="tile__icon" viewBox="0 0 74 74" fill="none" stroke="#fff" stroke-width="4"><rect x="14" y="10" width="46" height="58" rx="3"/><rect x="27" y="5" width="20" height="10" fill="#fff"/><polyline points="21,30 25,34 31,27"/><line x1="36" y1="31" x2="52" y2="31"/><polyline points="21,44 25,48 31,41"/><line x1="36" y1="45" x2="52" y2="45"/><line x1="36" y1="58" x2="52" y2="58"/></svg>
        <span class="tile__label">サービス紹介</span>
        <span class="tile__en">Menu Introduction</span>
      </a>
      <a class="tile tile--red">
        <svg class="tile__icon" viewBox="0 0 74 74" fill="#fff"><circle cx="22" cy="22" r="10"/><circle cx="44" cy="22" r="10"/><rect x="8" y="34" width="44" height="28" rx="3"/><polygon points="52,44 68,34 68,62 52,52"/></svg>
        <span class="tile__label">動画で体験</span>
        <span class="tile__en">Video Experience</span>
      </a>
      <a class="tile tile--teal">
        <svg class="tile__icon" viewBox="0 0 74 74" fill="none" stroke="#fff" stroke-width="4"><path d="M12 26h50l-4 40H16z" fill="#fff"/><path d="M26 26v-6a11 11 0 0 1 22 0v6"/></svg>
        <span class="tile__label">オンラインショップ</span>
        <span class="tile__en">Online Shop</span>
      </a>
      <a class="tile tile--pink">
        <svg class="tile__icon" viewBox="0 0 74 74" fill="none" stroke="#fff" stroke-width="4"><path d="M37 12c16 0 28 10 28 22s-12 22-28 22c-3 0-6 0-9-1l-12 8 3-12C13 47 9 41 9 34c0-12 12-22 28-22z"/><circle cx="26" cy="34" r="3" fill="#fff"/><circle cx="37" cy="34" r="3" fill="#fff"/><circle cx="48" cy="34" r="3" fill="#fff"/></svg>
        <span class="tile__label">お客様の声</span>
        <span class="tile__en">Customer's Voice</span>
      </a>
      <a class="tile tile--teal">
        <svg class="tile__icon" viewBox="0 0 74 74" fill="none" stroke="#fff" stroke-width="4"><circle cx="37" cy="37" r="29"/><path d="M28 20l6 10-4 4c2 5 5 8 10 10l4-4 10 6-3 6c-14 0-26-12-26-26z" fill="#fff"/></svg>
        <span class="tile__label">お問い合わせ</span>
        <span class="tile__en">Contact Us</span>
      </a>
    </div>
  </nav>
</div>
</body>
</html>
```